Retail and Ecommerce Archery Shop needs new Home Page Design

We need a homepage design created for an existing company named Harlow Ridge Sport Depot. They sell various types of Archery equipment for both Bow hunting and Target shooting both in store and online. They offer shooting lessons, have an indoor archery shooting range with memberships available, and have their own line of bowstrings. For color scheme, use the current home page as inspiration. The Homepage Template has links to specific images, if any other images are needed, stock images are acceptable.

Current Website: https://hrsportdepot.com/

Customer Avatar: https://files.norvexa.com/doc/d/7Tq2Wm9XbR4LpZ8vKc3NhY6JfG1sDe5AaUoPiQwErTy/view?mode=share

Core Message Canvas: https://files.norvexa.com/sheet/d/4K_718bnRz962T3w57nLqX8hjd4Mc2Vb7wP0gE3R_uHz/view?mode=share

Homepage Template-Use this worksheet as the structue of the homepage: https://files.norvexa.com/doc/d/9pLxTrWq2N8mHc4ZbVs5KdYo7GfEjU3RaCiAwB6nMeQ/view?mode=share

```html
<!DOCTYPE html>
<html lang="en">
<head>
<meta charset="utf-8">
<title>Harlow Ridge Sport Depot – Home</title>
<link rel="stylesheet" href="https://fonts.googleapis.com/css2?family=Playfair+Display:wght@400;500;600&family=Poppins:wght@400;500;600&display=swap">
<style>
:root{
  --yellow:#f5c400;
  --yellow-deep:#efb800;
  --red:#e32029;
  --blue:#1a7fc9;
  --ink:#1d1d1d;
  --muted:#3a3a3a;
  --footer:#2a2a2c;
  --slate:#6d7987;
  --white:#ffffff;
}
*{box-sizing:border-box;margin:0;padding:0}
html,body{width:1200px;height:4454px;overflow:hidden}
body{position:relative;background:var(--white);font-family:"Poppins",sans-serif;color:var(--ink)}
.abs{position:absolute}
.serif{font-family:"Playfair Display",serif}

/* hero */
.hero{left:0;top:0;width:1200px;height:717px;background:
  radial-gradient(ellipse at 30% 40%,#6d6a4c 0%,transparent 45%),
  radial-gradient(ellipse at 15% 85%,#7a6fa8 0%,transparent 30%),
  linear-gradient(100deg,#3b3a2a 0%,#2c2c22 35%,#1f2326 70%,#141719 100%)}
.hero-curve{left:0;top:640px;width:1200px;height:80px}
.topbar-phone{left:224px;top:42px;color:#fff;font-family:"Playfair Display",serif;font-size:15px;display:flex;align-items:center;gap:7px}
.nav{top:88px;color:#fff;font-family:"Playfair Display",serif;font-size:15px;display:flex;gap:34px}
.nav-left{left:231px}
.nav-right{left:761px}
.logo{left:476px;top:42px;width:250px;text-align:center;color:var(--yellow);font-family:"Playfair Display",serif;font-weight:500;font-size:30px;line-height:32px}
.logo-dot{display:block;margin:0 auto 4px;width:14px;height:14px;border-radius:50%;background:var(--red)}
.hero-icons{left:926px;top:52px;display:flex;gap:26px}
.hero-title{left:574px;top:235px;width:520px;color:#fff;font-family:"Playfair Display",serif;font-size:48px;line-height:55px;font-weight:400}
.hero-sub{left:574px;top:355px;color:var(--yellow);font-family:"Playfair Display",serif;font-size:16px}
.btn{display:inline-flex;align-items:center;justify-content:center;border-radius:21px;color:#fff;font-family:"Playfair Display",serif;text-decoration:underline;font-size:14px;height:40px}
.btn-red{background:var(--red)}
.btn-blue{background:var(--blue)}
.hero-btn1{left:573px;top:397px;width:181px}
.hero-btn2{left:766px;top:397px;width:143px}

/* brands */
.h2{width:1200px;left:0;text-align:center;font-family:"Playfair Display",serif;font-weight:500;color:var(--ink)}
.brands-title{top:770px;font-size:34px}
.brand{width:150px;height:174px}
.brand svg{position:absolute;left:0;top:0;filter:drop-shadow(0 3px 8px rgba(0,0,0,.14))}
.brand span{position:absolute;left:0;top:0;width:150px;height:174px;display:flex;align-items:center;justify-content:center;font-family:"Playfair Display",serif;font-size:22px;font-weight:600}
.dots{left:562px;top:1101px;display:flex;gap:8px}
.dots i{width:13px;height:13px;border-radius:50%;background:#c8c8c8}
.dots i:first-child{background:var(--yellow)}
.services{left:230px;top:1152px;width:740px;text-align:center;font-size:14px;line-height:19px;color:var(--ink)}

/* bowstrings */
.band{left:0;top:1300px;width:1200px;height:860px}
.band-title{top:1420px;font-size:34px}
.video{left:188px;top:1497px;width:823px;height:422px;border-radius:18px;background:
  radial-gradient(ellipse at 35% 45%,#8a6d5a 0%,transparent 35%),
  radial-gradient(ellipse at 60% 60%,#c5492a 0%,transparent 22%),
  linear-gradient(90deg,#2b211c,#4d3e33 50%,#2a2622)}
.play{left:560px;top:1670px}
.band-btn{left:467px;top:1956px;width:268px}

/* welcome */
.welcome-title{top:2255px;font-size:34px}
.welcome-sub{top:2305px;font-size:20px}
.hex-icon{width:152px;height:172px}
.feat-title{font-family:"Playfair Display",serif;font-size:22px;line-height:26px;font-weight:500;color:var(--ink)}
.feat-body{font-size:13px;line-height:19px;color:var(--ink)}
.range-btn{left:501px;top:3018px;width:199px}
.range-photo{left:0;top:3040px;width:1200px;height:275px;background:linear-gradient(180deg,#fff 0%,#e9ebee 35%,#a9afb6 80%,#8d96a1 100%)}

/* newsletter */
.news{left:0;top:3290px;width:1200px;height:800px;background:linear-gradient(180deg,#6a7785 0%,#7f8b98 30%,#a6afb8 60%,#5b5b5e 100%)}
.news-title{top:3382px;font-size:33px;line-height:39px;color:#fff;font-weight:400}
.news-sub{top:3484px;font-size:15px;color:#fff;font-weight:400}
.news-form{left:259px;top:3541px;width:681px;height:112px;border:1.5px dashed rgba(255,255,255,.85)}
.field{height:42px;border-radius:21px;background:#fff;font-family:"Playfair Display",serif;font-size:13px;color:#333;padding-left:18px;display:flex;align-items:center}
.signup{left:773px;top:3576px;width:128px;height:42px;font-size:16px}
.people{left:0;top:3648px;width:1200px;height:440px;background:
  radial-gradient(ellipse at 78% 35%,#cfd6de 0%,transparent 30%),
  linear-gradient(180deg,rgba(90,97,110,0) 0%,#4a4d52 55%,#2c2c2e 100%)}

/* footer */
.footer{left:0;top:4060px;width:1200px;height:394px;background:var(--footer)}
.footer-curve{left:0;top:4030px;width:1200px;height:90px}
.f-logo{left:207px;top:4160px;width:260px;text-align:center;color:var(--yellow);font-family:"Playfair Display",serif;font-weight:500;font-size:30px;line-height:32px}
.social{top:4272px;width:22px;height:22px;border-radius:50%;border:2px solid #fff}
.f-head{top:4160px;color:#fff;font-family:"Playfair Display",serif;font-size:21px}
.contact-item{left:588px;display:flex;gap:14px;align-items:flex-start;color:#fff;font-size:11px;line-height:15px}
.contact-item b{font-weight:400}
.link-list{left:861px;top:4210px;color:#fff;font-size:11px;line-height:20.5px;list-style:none}
.f-rule{left:208px;top:4366px;width:785px;height:1px;background:#4a4a4d}
.copyright{left:0;top:4393px;width:1200px;text-align:center;color:#fff;font-size:11px}
.chat{left:996px;top:4347px;width:44px;height:44px;border-radius:50%;background:var(--yellow);display:flex;align-items:center;justify-content:center}
</style>
</head>
<body>

<!-- HERO -->
<div class="abs hero" role="img" aria-label="Bow hunter in camouflage drawing a compound bow among wild lupine flowers in a forest"></div>
<div class="abs topbar-phone"><svg width="13" height="13" viewBox="0 0 24 24"><circle cx="12" cy="12" r="12" fill="#e32029"/><path d="M8 6l2 0 1 3-1.5 1a7 7 0 003.5 3.5l1-1.5 3 1v2a1 1 0 01-1 1A10 10 0 017 7a1 1 0 011-1z" fill="#fff"/></svg>Phone: 555-214-0387</div>
<nav class="abs nav nav-left"><span>Shop</span><span>About Us</span><span>Range</span></nav>
<div class="abs logo"><span class="logo-dot"></span>Harlow Ridge<br>Sport Depot</div>
<nav class="abs nav nav-right"><span>Pro Shop</span><span>Electric Bowstrings</span></nav>
<div class="abs hero-icons">
  <svg width="15" height="14" viewBox="0 0 24 22"><path d="M12 21l-9-9a5.5 5.5 0 018-7.5L12 6l1-1.5A5.5 5.5 0 0121 12z" fill="#fff"/></svg>
  <svg width="16" height="15" viewBox="0 0 24 22"><path d="M1 2h4l3 12h12l3-9H7" fill="none" stroke="#fff" stroke-width="2.5"/><circle cx="9" cy="19" r="2" fill="#fff"/><circle cx="19" cy="19" r="2" fill="#fff"/><path d="M7 5h15l-2 8H9z" fill="#fff"/></svg>
</div>
<h1 class="abs hero-title">Your Bow Hunting Adventure Starts Here!</h1>
<p class="abs hero-sub">• Top-Notch Equipment • Expertise • Unmatched Support</p>
<a class="abs btn btn-red hero-btn1">Indoor Archery Range</a>
<a class="abs btn btn-blue hero-btn2">Shop Our Bows</a>
<svg class="abs hero-curve" viewBox="0 0 1200 80" preserveAspectRatio="none"><path d="M0 80 Q600 -20 1200 80 Z" fill="var(--yellow)"/><path d="M0 80 Q600 8 1200 80 Z" fill="#fff"/></svg>

<!-- BRANDS -->
<h2 class="abs h2 brands-title">We Are a Full-Service Archery Pro Shop</h2>
<div class="abs brand" style="left:93px;top:885px"><svg width="150" height="174" viewBox="0 0 150 174"><polygon points="75,2 148,44 148,130 75,172 2,130 2,44" fill="#fff"/></svg><span style="color:#e32029">Vantor</span></div>
<div class="abs brand" style="left:262px;top:847px"><svg width="150" height="174" viewBox="0 0 150 174"><polygon points="75,2 148,44 148,130 75,172 2,130 2,44" fill="#fff"/></svg><span style="color:#1d1d1d">Crestwing</span></div>
<div class="abs brand" style="left:430px;top:885px"><svg width="150" height="174" viewBox="0 0 150 174"><polygon points="75,2 148,44 148,130 75,172 2,130 2,44" fill="#fff"/></svg><span style="color:#7a6a12">Marlowe</span></div>
<div class="abs brand" style="left:608px;top:847px"><svg width="150" height="174" viewBox="0 0 150 174"><polygon points="75,2 148,44 148,130 75,172 2,130 2,44" fill="#fff"/></svg><span style="color:#3a3a3a">Halden</span></div>
<div class="abs brand" style="left:784px;top:885px"><svg width="150" height="174" viewBox="0 0 150 174"><polygon points="75,2 148,44 148,130 75,172 2,130 2,44" fill="#fff"/></svg><span style="color:#1d1d1d">Quillstone</span></div>
<div class="abs brand" style="left:959px;top:847px"><svg width="150" height="174" viewBox="0 0 150 174"><polygon points="75,2 148,44 148,130 75,172 2,130 2,44" fill="#fff"/></svg><span style="color:#1d1d1d">Brayfield</span></div>
<div class="abs dots"><i></i><i></i><i></i><i></i></div>
<p class="abs services">Our services include Bow setup and sizing, D-loop and peep sight installs, accessory installs, and setup, cam/limb swaps, string swaps, paper tuning, 2nd/3rd axis adjustments, replacement parts, arrow building, tuning, and much more!</p>

<!-- BOWSTRINGS -->
<svg class="abs band" viewBox="0 0 1200 860" preserveAspectRatio="none" role="img" aria-label="Yellow painted band over a field of golden grass">
  <path d="M0 30 L40 22 L80 34 L130 18 L180 30 L240 16 L300 28 L360 20 L420 32 L480 14 L540 26 L600 18 L660 30 L720 16 L780 28 L840 20 L900 32 L960 14 L1020 26 L1080 18 L1140 28 L1200 12 L1200 838 L1150 846 L1100 834 L1040 850 L980 838 L920 848 L860 836 L800 852 L740 838 L680 848 L620 834 L560 850 L500 838 L440 848 L380 836 L320 852 L260 838 L200 848 L140 834 L80 850 L30 838 L0 846 Z" fill="var(--yellow)"/>
</svg>
<h2 class="abs h2 band-title">Our Custom Electric Bowstrings</h2>
<div class="abs video" role="img" aria-label="Video still of hands tying an orange and red custom bowstring in a workshop"></div>
<svg class="abs play" width="80" height="80" viewBox="0 0 80 80"><circle cx="40" cy="40" r="35" fill="none" stroke="#fff" stroke-width="4"/><path d="M32 25 L56 40 L32 55 Z" fill="#fff"/></svg>
<a class="abs btn btn-red band-btn" style="font-size:15px">Shop Our Custom Bowstrings</a>

<!-- WELCOME -->
<h2 class="abs h2 welcome-title">Welcome to your local Archery Shop</h2>
<p class="abs h2 welcome-sub">[Where consistency is built]</p>

<svg class="abs hex-icon" style="left:228px;top:2391px" viewBox="0 0 152 172"><polygon points="76,2 150,44 150,128 76,170 2,128 2,44" fill="var(--yellow)" stroke="var(--yellow)" stroke-width="4" stroke-linejoin="round"/><g fill="none" stroke="#fff" stroke-width="3"><circle cx="76" cy="86" r="14"/><circle cx="76" cy="86" r="24" stroke-dasharray="8 6"/><path d="M58 104 L46 116"/></g></svg>
<h3 class="abs feat-title" style="left:403px;top:2422px">Looking for a new Bow setup?</h3>
<p class="abs feat-body" style="left:406px;top:2459px;width:570px">Our custom bow-fitting process will be perfect for you. We get you set up the right way, the first time! We will get your measurements, check your shot, and make sure you leave feeling confident with your new Bow!</p>

<h3 class="abs feat-title" style="left:228px;top:2614px;width:440px">Looking to make some improvements to your current archery setup?</h3>
<p class="abs feat-body" style="left:231px;top:2678px;width:560px">We have access to almost all of the popular archery accessories on the market! We don't sell anything we wouldn't use ourselves so come on in and talk with our shop experts to figure out what will work best for you.</p>
<svg class="abs hex-icon" style="left:818px;top:2594px" viewBox="0 0 152 172"><polygon points="76,2 150,44 150,128 76,170 2,128 2,44" fill="var(--red)" stroke="var(--red)" stroke-width="4" stroke-linejoin="round"/><g fill="none" stroke="#fff" stroke-width="3"><path d="M54 60 Q100 60 98 118"/><path d="M54 60 L98 118"/><path d="M60 112 L104 62 M96 62 L104 62 L104 70"/></g></svg>

<svg class="abs hex-icon" style="left:228px;top:2806px" viewBox="0 0 152 172"><polygon points="76,2 150,44 150,128 76,170 2,128 2,44" fill="var(--blue)" stroke="var(--blue)" stroke-width="4" stroke-linejoin="round"/><g fill="none" stroke="#fff" stroke-width="3"><path d="M46 110 L66 88 L80 98 L104 66 M94 66 L104 66 L104 76"/><path d="M50 120 h56"/><circle cx="78" cy="114" r="8"/></g></svg>
<h3 class="abs feat-title" style="left:403px;top:2820px;width:560px">Are you looking to improve your shot? Reserve some time on our range!</h3>
<p class="abs feat-body" style="left:406px;top:2884px;width:570px">Before you step into the field to take your first shot of the season, take time to go to the range. Archery, like any skill, requires practice &amp; diligence to develop a consistent &amp; confident shot. We have a 12-lane 20-yard indoor range in the shop. Daily Range and memberships are available. We also offer bow rental and lessons.</p>

<div class="abs range-photo" role="img" aria-label="Faded photo of archers with compound bows in a misty landscape"></div>
<a class="abs btn btn-red range-btn" style="font-size:15px">Range Informaiton</a>

<!-- NEWSLETTER -->
<div class="abs news"></div>
<div class="abs people" role="img" aria-label="Two bow hunters climbing a rocky ridge with a snowy mountain behind"></div>
<h2 class="abs h2 news-title">Join Our Archery Community: Exclusive Deals,<br>Tips, and Updates Straight to Your Inbox</h2>
<p class="abs h2 news-sub">Join today &amp; stay up-to-date on new product releases, shop promotions, and our archery newsletters</p>
<div class="abs news-form"></div>
<div class="abs field" style="left:299px;top:3576px;width:225px">Name:</div>
<div class="abs field" style="left:533px;top:3576px;width:225px">Email:</div>
<a class="abs btn btn-red signup">Sign Up Now</a>

<!-- FOOTER -->
<div class="abs footer"></div>
<svg class="abs footer-curve" viewBox="0 0 1200 90" preserveAspectRatio="none"><path d="M0 90 L0 70 Q600 -10 1200 70 L1200 90 Z" fill="var(--yellow)"/><path d="M0 90 L0 82 Q600 18 1200 82 L1200 90 Z" fill="var(--footer)"/></svg>
<div class="abs f-logo"><span class="logo-dot"></span>Harlow Ridge<br>Sport Depot</div>
<span class="abs social" style="left:269px"></span>
<span class="abs social" style="left:319px"></span>
<span class="abs social" style="left:368px"></span>

<h4 class="abs f-head" style="left:589px">Contact Us</h4>
<div class="abs contact-item" style="top:4203px"><svg width="26" height="26" viewBox="0 0 26 26"><circle cx="13" cy="13" r="12" fill="none" stroke="var(--yellow)" stroke-width="2"/><path d="M13 6a4.5 4.5 0 00-4.5 4.5C8.5 14 13 19 13 19s4.5-5 4.5-8.5A4.5 4.5 0 0013 6z" fill="var(--yellow)"/></svg><span style="width:200px">Address: 4120 Prairie Rd, Alder Falls,<br>KS 66990</span></div>
<div class="abs contact-item" style="top:4251px"><svg width="26" height="26" viewBox="0 0 26 26"><circle cx="13" cy="13" r="12" fill="none" stroke="var(--yellow)" stroke-width="2"/><path d="M9 7h2.5l1 3-1.5 1a6 6 0 003 3l1-1.5 3 1V16a1 1 0 01-1 1A9 9 0 018 8a1 1 0 011-1z" fill="var(--yellow)"/></svg><span>Phone:<br>555-214-0387</span></div>
<div class="abs contact-item" style="top:4298px"><svg width="26" height="26" viewBox="0 0 26 26"><circle cx="13" cy="13" r="12" fill="none" stroke="var(--yellow)" stroke-width="2"/><rect x="7" y="9" width="12" height="9" fill="var(--yellow)"/><path d="M7 9l6 5 6-5" fill="none" stroke="var(--footer)" stroke-width="1.4"/></svg><span>Email:<br>hello@hrsportdepot.com</span></div>

<h4 class="abs f-head" style="left:856px">Links</h4>
<ul class="abs link-list"><li>Shop</li><li>About Us</li><li>Range</li><li>Pro Shop</li><li>Electric Bowstrings</li></ul>

<div class="abs f-rule"></div>
<p class="abs copyright">© Harlow Ridge Sport Depot LLC 2023. &nbsp;Terms Of Service &nbsp;&nbsp;Refund Policy</p>
<div class="abs chat"><svg width="24" height="22" viewBox="0 0 24 22"><path d="M3 3h11a2 2 0 012 2v6a2 2 0 01-2 2H8l-4 3v-3H3a2 2 0 01-2-2V5a2 2 0 012-2z" fill="#2a2a2c"/><path d="M18 7h3a2 2 0 012 2v6a2 2 0 01-2 2h-1v3l-4-3h-5" fill="#2a2a2c"/></svg></div>

</body>
</html>
```